business card for a massage therapy practice named 'Meadow and Willow Massage Studio'

I really need a trendy, yet easy on the eyes business card to complement my logo. Ideally with some gold or rose gold foil work.

My uploaded file of the logo I have in horizontal but I have a vertical version as well. Another color that is used in the website is a blush pink here and there. I'd like to see some trendy tropical leaves in the design.

```html
<!DOCTYPE html>
<html lang="en">
<head>
<meta charset="utf-8">
<title>Meadow and Willow Massage Studio – Business Card</title>
<link rel="stylesheet" href="https://fonts.googleapis.com/css2?family=Marcellus&family=Crimson+Pro:wght@400;500&display=swap">
<style>
  :root {
    --backdrop: #efedea;
    --card-white: #ffffff;
    --ink-green: #2f5a4c;
    --ink-grey: #3c3c3c;
    --mint: #82cdb5;
    --leaf-pale: #eef7d2;
    --leaf-light: #d4ec9c;
    --leaf-mid: #a8d85a;
    --leaf-deep: #6cbc34;
    --leaf-dark: #58a82a;
    --logo-ink: #1f2a22;
    --blush: #f4dede;
  }
  * { box-sizing: border-box; margin: 0; padding: 0; }
  html, body { width: 1200px; height: 1200px; overflow: hidden; }
  body {
    background: var(--backdrop);
    font-family: "Crimson Pro", Georgia, serif;
    display: flex;
    align-items: center;
    justify-content: center;
    gap: 60px;
  }
  .card {
    width: 420px;
    height: 720px;
    position: relative;
    overflow: hidden;
    box-shadow: 0 14px 30px rgba(0,0,0,0.18);
  }

  /* Front */
  .card-front { background: var(--card-white); }
  .spa-photo {
    position: absolute; left: 0; top: 0;
    width: 100%; height: 250px;
    background:
      linear-gradient(180deg, transparent 78%, var(--card-white) 100%),
      radial-gradient(ellipse 40% 35% at 68% 68%, #ffffff 0%, #f6f7ec 45%, transparent 100%),
      radial-gradient(ellipse 30% 45% at 0% 10%, var(--leaf-dark) 0%, transparent 100%),
      radial-gradient(ellipse 28% 40% at 100% 5%, var(--leaf-dark) 0%, transparent 100%),
      linear-gradient(160deg, var(--leaf-deep) 0%, var(--leaf-mid) 40%, var(--leaf-light) 75%, var(--leaf-pale) 100%);
  }
  .contact {
    position: absolute; left: 0; right: 0; top: 320px;
    text-align: center;
    color: var(--ink-grey);
  }
  .contact-name {
    font-family: "Marcellus", Georgia, serif;
    font-size: 56px;
    font-weight: 400;
    color: var(--ink-green);
    line-height: 1;
  }
  .contact-role { font-size: 24px; line-height: 1.4; margin-top: 6px; }
  .contact-address { font-size: 24px; line-height: 1.4; margin-top: 26px; }
  .contact-lines { font-size: 24px; line-height: 1.4; margin-top: 22px; }
  .footer-rule {
    position: absolute; left: 0; right: 0; bottom: 52px;
    height: 3px; background: var(--mint);
  }
  .footer-band {
    position: absolute; left: 0; right: 0; bottom: 0;
    height: 42px; background: var(--mint);
  }

  /* Back */
  .card-back {
    background:
      linear-gradient(90deg, var(--leaf-mid) 0%, var(--leaf-light) 30%, var(--leaf-pale) 50%, var(--leaf-light) 70%, var(--leaf-mid) 100%);
  }
  .leaf-frame {
    position: absolute; inset: 0;
    background:
      radial-gradient(ellipse 45% 28% at 0% 12%, var(--leaf-dark) 0%, rgba(108,188,52,0.6) 50%, transparent 100%),
      radial-gradient(ellipse 40% 30% at 0% 62%, var(--leaf-deep) 0%, rgba(108,188,52,0.5) 50%, transparent 100%),
      radial-gradient(ellipse 42% 26% at 100% 18%, var(--leaf-dark) 0%, rgba(108,188,52,0.55) 50%, transparent 100%),
      radial-gradient(ellipse 45% 30% at 100% 88%, var(--leaf-deep) 0%, rgba(108,188,52,0.5) 50%, transparent 100%);
  }
  .blush-edge {
    position: absolute; left: 0; right: 0; bottom: 0;
    height: 8px; background: var(--blush);
  }
  .brand {
    position: absolute; left: 50%; top: 50%;
    transform: translate(-50%, -50%) rotate(-90deg);
    display: flex; align-items: center; gap: 16px;
    white-space: nowrap;
  }
  .brand-mark {
    width: 22px; height: 22px; border-radius: 50%;
    background: var(--logo-ink);
  }
  .brand-name {
    font-size: 32px; font-weight: 500;
    color: var(--logo-ink);
    letter-spacing: 0.5px;
  }
</style>
</head>
<body>
  <section class="card card-front">
    <div class="spa-photo" role="img" aria-label="Spa still life with orchids, rolled white towels, a tea light and lotion bottles, framed by tropical palm leaves on a soft green background"></div>
    <div class="contact">
      <h1 class="contact-name">Evan Hale</h1>
      <p class="contact-role">Director</p>
      <p class="contact-address">Dummy city<br>Dummy Country Land</p>
      <p class="contact-lines">1-555-014-2288<br>evan@meadowandwillow.com<br>www.meadowandwillow.com</p>
    </div>
    <div class="footer-rule"></div>
    <div class="footer-band"></div>
  </section>

  <section class="card card-back">
    <div class="leaf-frame" role="img" aria-label="Tropical palm leaves framing the card edges over a watercolour green background"></div>
    <div class="brand">
      <span class="brand-mark"></span>
      <span class="brand-name">Meadow and Willow Massage Studio</span>
    </div>
    <div class="blush-edge"></div>
  </section>
</body>
</html>
```